Business Card Design

My business is writing crime novels to entertain readers. I write legal thrillers and mysteries. I need a card for publishers, agents, other authors, and media.

Industry/Entity Type

Legal

Contact Information for Business Card

Paul Ostrander
www.ostranderthrillers.example
paulbostrander@mailbox.example
0064 27 5139427

```html
<!DOCTYPE html>
<html lang="en">
<head>
<meta charset="utf-8">
<title>Paul Ostrander – Business Card</title>
<link href="https://fonts.googleapis.com/css2?family=Questrial&display=swap" rel="stylesheet">
<style>
  :root {
    --canvas-bg: #ffffff;
    --card-bg: #ffffff;
    --ink: #2b303b;
    --ink-soft: #6b707a;
    --rule-dark: #4a505c;
    --band-top: #b9bdc4;
    --band-mid: #5d626c;
    --band-bottom: #454a54;
    --band-text: #ffffff;
    --portrait-light: #eef0f2;
    --portrait-mid: #b4b6ba;
    --portrait-dark: #2c2d30;
  }
  * { margin: 0; padding: 0; box-sizing: border-box; }
  html, body {
    width: 848px;
    height: 1200px;
    overflow: hidden;
    background: var(--canvas-bg);
    font-family: "Questrial", "Century Gothic", sans-serif;
  }
  .business-card {
    position: absolute;
    left: 64px;
    top: 412px;
    width: 720px;
    height: 376px;
    background: var(--card-bg);
    overflow: hidden;
  }
  .card-name {
    position: absolute;
    left: 39px;
    top: 30px;
    font-size: 29px;
    font-weight: 400;
    color: var(--ink);
    letter-spacing: 0.2px;
  }
  .card-role {
    position: absolute;
    left: 39px;
    top: 66px;
    font-size: 17px;
    color: var(--ink-soft);
  }
  .card-rule {
    position: absolute;
    left: 0;
    top: 99px;
    width: 520px;
    height: 3px;
    background: linear-gradient(to right, var(--rule-dark) 0%, var(--rule-dark) 40%, rgba(74,80,92,0) 100%);
  }
  .card-contact {
    position: absolute;
    left: 44px;
    top: 148px;
    font-size: 19px;
    line-height: 26px;
    color: var(--ink);
  }
  .card-contact .contact-email { color: var(--ink-soft); }
  .web-band {
    position: absolute;
    left: 0;
    top: 257px;
    width: 466px;
    height: 92px;
    background: linear-gradient(to bottom, var(--band-top) 0%, var(--band-mid) 14%, var(--band-bottom) 100%);
    display: flex;
    align-items: center;
    justify-content: center;
    padding-top: 8px;
  }
  .web-address {
    font-size: 23px;
    color: var(--band-text);
    letter-spacing: 0.3px;
  }
  .portrait {
    position: absolute;
    left: 460px;
    top: 0;
    width: 260px;
    height: 376px;
    background:
      radial-gradient(ellipse 70% 55% at 50% 95%, var(--portrait-dark) 0%, var(--portrait-dark) 55%, rgba(44,45,48,0) 75%),
      linear-gradient(to bottom, var(--portrait-light) 0%, var(--portrait-mid) 100%);
  }
</style>
</head>
<body>
  <div class="business-card">
    <div class="card-name">Paul Ostrander</div>
    <div class="card-role">Crime Novelist</div>
    <div class="card-rule"></div>
    <div class="card-contact">
      <div class="contact-phone">0064 27 5139427</div>
      <div class="contact-email">paulbostrander@mailbox.example</div>
    </div>
    <div class="web-band">
      <span class="web-address">www.ostranderthrillers.example</span>
    </div>
    <div class="portrait" role="img" aria-label="Portrait photo of the author in a dark jacket and white shirt"></div>
  </div>
</body>
</html>
```